Based on your KWP party invitation. Could you please change to characters to be Afro Carribbean characters?

• Logo Attached and wording below.

Northvale Fairway Society 20th Anniversary
Dinner and Dance
Saturday 30th November 2013
Pellow and Greaves Banqueting Suite
Sundial Lodge London Marwick
Tealby Street
London
QZ7 4XJ
From :7PM to 2AM
Dress Code: Black Tie and Ball Gowns
Dinner Served: 8.PM SHARP
DJ: "Dell" form Manhattan
Live Jazz Band
Magicians
Mystery Guest Speaker
Overnight Accommodation available
Nearest Tube: Hadley Crescent (Marlow Line)
Parking: Facilities available in hotel and adjacent (charges apply)
TICKETS £65. 00
For more information or to reserve tickets, please visit: www.nvfs-example.co.uk

```html
<!DOCTYPE html>
<html lang="en">
<head>
<meta charset="utf-8">
<title>Northvale Fairway Society – 20th Anniversary Dinner and Dance Invitation</title>
<link rel="stylesheet" href="https://fonts.googleapis.com/css2?family=Arimo&family=Cormorant+Garamond:ital,wght@1,500;1,600&family=Mulish:wght@700;800&display=swap">
<style>
  :root {
    --page-bg: #ffffff;
    --label: #1a1a1a;
    --back-black: #0a0b0c;
    --back-brown: #4a1d14;
    --back-text: #4a1a18;
    --title-red: #7a1e1e;
    --title-orange: #e97f22;
    --band-black: #0c0c0c;
    --title-ink: #6b2418;
    --inside-bg: #54271c;
    --inside-ink: #eaa24f;
  }
  * { margin: 0; padding: 0; box-sizing: border-box; }
  html, body { width: 1200px; height: 897px; overflow: hidden; background: var(--page-bg); }
  .sheet { position: relative; width: 1200px; height: 897px; }

  .label {
    position: absolute;
    font-family: "Arimo", Arial, sans-serif;
    font-size: 30px;
    color: var(--label);
    transform: translateX(-50%);
    white-space: nowrap;
  }
  .label--back { left: 321px; top: 48px; }
  .label--title { left: 803px; top: 42px; }
  .label--inside { left: 518px; top: 476px; }

  .panel { position: absolute; overflow: hidden; }

  /* Back page 4 */
  .back { left: 76px; top: 92px; width: 511px; height: 365px; background: var(--back-black); }
  .back__swoosh { position: absolute; inset: 0; }
  .back__text {
    position: absolute; left: 0; width: 511px; text-align: center;
    font-family: "Arimo", Arial, sans-serif; color: var(--back-text);
    font-size: 20px; line-height: 25px;
  }
  .back__tickets { top: 136px; left: 52px; }
  .back__info { top: 202px; left: 2px; }

  /* Title page 1 */
  .cover {
    left: 595px; top: 91px; width: 511px; height: 364px;
    background: linear-gradient(160deg, var(--title-red) 0%, #a8401c 35%, #cf6220 70%, var(--title-orange) 100%);
  }
  .cover__art {
    position: absolute; left: 150px; top: 40px; width: 340px; height: 320px;
    border-radius: 48% 48% 40% 40%;
    background: radial-gradient(ellipse at 50% 45%, rgba(240,140,60,0.55), rgba(230,120,50,0.15) 60%, rgba(0,0,0,0) 75%);
  }
  .cover__band {
    position: absolute; left: 0; top: 29px; width: 511px; height: 73px;
    background: var(--band-black);
    display: flex; align-items: center;
  }
  .cover__mark {
    width: 40px; height: 40px; margin-left: 48px; border-radius: 50%;
    background: var(--title-red);
  }
  .cover__org {
    margin-left: 33px;
    font-family: "Mulish", "Century Gothic", sans-serif; font-weight: 800;
    font-size: 19px; color: var(--title-red);
  }
  .cover__headline {
    position: absolute; left: 0; width: 511px; text-align: center;
    font-family: "Mulish", "Century Gothic", sans-serif; font-weight: 800;
    color: var(--title-ink);
  }
  .cover__anniversary { top: 163px; font-size: 46px; letter-spacing: -0.5px; left: 2px; }
  .cover__event { top: 256px; font-size: 25px; left: -4px; }

  /* Inside pages 2 and 3 */
  .inside { top: 515px; width: 511px; height: 365px; background: var(--inside-bg); }
  .inside--left { left: 76px; }
  .inside--right { left: 598px; }
  .inside__art {
    position: absolute; left: 120px; top: 20px; width: 320px; height: 310px;
    border-radius: 50%;
    background: radial-gradient(ellipse at 50% 45%, rgba(120,55,38,0.8), rgba(95,44,31,0.35) 60%, rgba(0,0,0,0) 75%);
  }
  .inside__text {
    position: absolute;
    font-family: "Cormorant Garamond", "Monotype Corsiva", serif;
    font-style: italic; font-weight: 600;
    color: var(--inside-ink); font-size: 23px; line-height: 26px;
    white-space: nowrap;
  }
  .inside__text p { margin: 0; }
  .gap { height: 26px; }
  .details { left: 19px; top: 20px; }
  .details .served { padding-left: 63px; }
  .details .small { font-size: 21px; }
  .venue { left: 0; top: 44px; width: 511px; text-align: center; }
  .venue .time { margin-left: -55px; margin-top: 26px; }
  .venue .address { margin-top: 18px; }
  .venue .dress { margin-top: 16px; font-size: 25px; line-height: 29px; }
</style>
</head>
<body>
<main class="sheet">
  <div class="label label--back">Back page 4</div>
  <div class="label label--title">Title page 1</div>
  <div class="label label--inside">inside pages 2 and 3</div>

  <section class="panel back" aria-label="Back page">
    <svg class="back__swoosh" width="511" height="365" viewBox="0 0 511 365" aria-hidden="true">
      <defs>
        <linearGradient id="swooshFill" x1="0" y1="0" x2="1" y2="0">
          <stop offset="0" stop-color="#0a0b0c" stop-opacity="0"/>
          <stop offset="0.6" stop-color="#2a120d"/>
          <stop offset="1" stop-color="#5a2416"/>
        </linearGradient>
      </defs>
      <path d="M511 0 C420 20 360 40 370 120 C380 200 300 260 240 365 L511 365 Z" fill="url(#swooshFill)"/>
    </svg>
    <p class="back__text back__tickets">TICKETS £65. 00</p>
    <p class="back__text back__info">For more information;<br>or to reserve tickets,<br>please visit: www.nvfs-example.co.uk</p>
  </section>

  <section class="panel cover" aria-label="Title page">
    <div class="cover__art" role="img" aria-label="Stylised African Caribbean mask illustration"></div>
    <div class="cover__band">
      <span class="cover__mark"></span>
      <span class="cover__org">Northvale Fairway Society</span>
    </div>
    <h1 class="cover__headline cover__anniversary">20th Anniversary</h1>
    <h2 class="cover__headline cover__event">Dinner and Dance</h2>
  </section>

  <section class="panel inside inside--left" aria-label="Inside page 2">
    <div class="inside__art" role="img" aria-label="Faint mask illustration watermark"></div>
    <div class="inside__text details">
      <p class="served">Dinner Served: 8.PM SHARP</p>
      <div class="gap"></div>
      <p>DJ: "Dell" form Manhattan</p>
      <p>Live Jazz Band</p>
      <p>Magicians</p>
      <p>Mystery Guest Speaker</p>
      <div class="gap"></div>
      <p>Overnight Accommodation available</p>
      <div class="gap"></div>
      <p class="small">Nearest Tube: Hadley Crescent (Marlow Line)</p>
      <p>Parking: Facilities available in hotel and</p>
      <p>adjacent (charges apply)</p>
    </div>
  </section>

  <section class="panel inside inside--right" aria-label="Inside page 3">
    <div class="inside__art" role="img" aria-label="Faint mask illustration watermark"></div>
    <div class="inside__text venue">
      <p style="margin-left:-55px">Saturday 30th November 2013</p>
      <p class="time">From :7PM to 2AM</p>
      <div class="address">
        <p>Pellow and Greaves Banqueting Suite</p>
        <p>Sundial Lodge London Marwick</p>
        <p>Tealby Street</p>
        <p>London QZ7 4XJ</p>
      </div>
      <div class="dress">
        <p>Dress Code:</p>
        <p>Black Tie and Ball Gowns</p>
      </div>
    </div>
  </section>
</main>
</body>
</html>
```